zOS app - Personal finance : Loan Calculator

Hi,
I need an app design for an zOS application that respects the last Plumora guidelines :
https://devs.plumora.com/os/interface-rules/graphics/app-icon/

I speak english and french.

Design should include logo, splashscreen and 4 main features as detailed further.

This application is a loan calculator that computes monthly payments, amortization tables, credit capacity.

App desc, screens and old logo here : https://apps.plumora.com/us/app/debt-path-housing-estimator/id584213097?mt=8

1. SPIRIT
The ideas to express in the design : simplicity, reliability, efficiency.
Use of graphics instead of words/number is always better.

2. ICON
No text, no letter in the logo.
Existing logo is not modern, too detailed.

3. SPLASHSCREEN

4. COLOR / Design style
ZOS 10 style
Modern colours
If you need one color as base use the blue

5. FEATURES/APP PAGES
Attached are the current screens to adapt with the new design :

Must Have:
- Loan Calculator (1screen uploaded in 2 parts)
- Loan Amortization : yearly table, monthly table and export (2 screens roughly the same +1)
- Saved Loans (1 screen), feature improvement could be to display what is left to pay for all loans, see saved loans idea 1 and 2 (I prefer the design of idea 1).
- Credit Capacity (1 screen uploaded in 2 parts), see also the inspiration file to propose a more visual interface (with chart/graphics)

Nice to have :
- refinance calculator (1 screen uploaded in 2 parts)
- Market rates table (1 screen)

Target Market(s)

1. Professionals in finance, real estate, car where a loan can be proposed to their customers -
2. Individuals that want to apply for a loan

Industry/Entity Type

Loan

Font styles to use
Serif
Sans Serif

Requirements
Must have
• Icon (see App Icon Guidelines in uploaded files)
• Splashscreen
• 4 Top features : Loan Calculator, Loan amortization with export, Credit capacity, Saved loans.
Nice to have
• Other screens : Refinance calculator, Market rates table
• New ideas of features / interactions
Should not have
• skeumorphism
• a total rupture from the current design : current users of the app should enjoy the new design and recognize the app without being lost (or not if you have arguments)

```html
<!DOCTYPE html>
<html lang="en">
<head>
<meta charset="utf-8">
<title>Loan Calculator</title>
<link rel="stylesheet" href="https://fonts.googleapis.com/css2?family=Montserrat:wght@400;600&family=Nunito+Sans:wght@300;400&display=swap">
<style>
  :root{
    --stage:#1d8fd1;
    --stage-deep:#1a74c4;
    --header:#66c7e2;
    --accent:#45bde0;
    --paper:#ffffff;
    --ink:#4a4a4a;
    --ink-soft:#8a8a8a;
    --rule:#e6e6e6;
    --field-line:#3a3a3a;
    --capital:#fbad4c;
    --interest:#f4815e;
    --insurance:#f06ea2;
    --donut-core:#f4f4f4;
  }
  *{box-sizing:border-box;margin:0;padding:0}
  html,body{width:1200px;height:864px;overflow:hidden}
  body{
    background:linear-gradient(135deg,var(--stage) 0%,var(--stage-deep) 100%);
    font-family:"Nunito Sans",Arial,sans-serif;
    color:var(--ink);
    position:relative;
  }
  .app-screen{
    position:absolute;left:390px;top:40px;width:420px;height:784px;
    background:var(--paper);
    box-shadow:0 20px 50px rgba(0,40,90,.35);
    display:flex;flex-direction:column;overflow:hidden;
  }
  .app-header{background:var(--header);color:#fff;height:96px;padding:6px 14px 0}
  .status-bar{display:flex;justify-content:space-between;align-items:center;font-size:11px;height:18px}
  .status-bar .carrier{display:flex;align-items:center;gap:4px}
  .status-bar .battery{display:flex;align-items:center;gap:4px}
  .battery-cell{width:22px;height:10px;border:1px solid #fff;border-radius:2px;padding:1px}
  .battery-cell span{display:block;width:100%;height:100%;background:#fff}
  .title-row{display:flex;align-items:center;justify-content:center;position:relative;height:58px}
  .app-title{font-family:"Montserrat",Arial,sans-serif;font-weight:600;font-size:17px;letter-spacing:2px}
  .share-button{position:absolute;right:2px;top:16px;width:26px;height:26px}

  .loan-form{padding:18px 22px 0}
  .project-name{color:var(--accent);font-size:22px;font-weight:400;margin-bottom:10px}
  .field{display:flex;justify-content:space-between;align-items:flex-end;height:46px;border-bottom:1px solid var(--rule);font-size:13px;letter-spacing:.3px}
  .field-label{padding-bottom:9px;color:var(--ink)}
  .field-value{min-width:110px;text-align:right;border-bottom:2px solid var(--field-line);padding-bottom:4px;margin-bottom:6px;font-size:14px}
  .term-tabs{display:flex;gap:22px}
  .term-tab{padding-bottom:9px;color:var(--ink)}
  .term-tab.is-active{color:var(--accent);border-bottom:2px solid var(--accent);padding-bottom:7px}

  .payment-summary{padding:22px 22px 0}
  .monthly-payment{color:var(--accent);font-size:22px;text-align:center}
  .breakdown{display:flex;align-items:center;justify-content:center;gap:30px;margin-top:14px}
  .legend{list-style:none;font-size:13px;color:var(--ink-soft);line-height:24px}
  .legend li{display:flex;align-items:center;gap:10px}
  .legend .dot{width:6px;height:6px;border-radius:50%}
  .dot.insurance{background:var(--insurance)}
  .dot.capital{background:var(--capital)}
  .dot.interest{background:var(--interest)}

  .totals{margin:18px 0 0;border-top:1px solid var(--rule);padding:14px 22px;font-size:13px;line-height:20px;text-align:center;letter-spacing:.3px}
  .totals + .totals{margin-top:0}

  .tab-bar{margin-top:auto;height:62px;border-top:1px solid var(--rule);display:flex}
  .tab-item{flex:1;display:flex;flex-direction:column;align-items:center;justify-content:center;gap:4px;font-size:11px;color:var(--ink-soft);position:relative}
  .tab-item svg{width:24px;height:22px}
  .tab-item.is-active{color:var(--ink)}
  .tab-item.is-active::before{content:"";position:absolute;top:0;left:50%;width:24px;height:3px;margin-left:-12px;background:var(--accent)}
</style>
</head>
<body>
  <main class="app-screen">
    <header class="app-header">
      <div class="status-bar">
        <span class="carrier">●●●●● Carrio
          <svg width="12" height="10" viewBox="0 0 12 10"><path d="M1 4a7 7 0 0 1 10 0M3 6a4 4 0 0 1 6 0" stroke="#fff" stroke-width="1.3" fill="none"/><circle cx="6" cy="8.3" r="1.1" fill="#fff"/></svg>
        </span>
        <span class="clock">9:41 AM</span>
        <span class="battery">100% <span class="battery-cell"><span></span></span></span>
      </div>
      <div class="title-row">
        <h1 class="app-title">LOAN CALCULATOR</h1>
        <svg class="share-button" viewBox="0 0 26 26"><circle cx="13" cy="13" r="11.5" fill="none" stroke="#fff" stroke-width="1.6"/><path d="M13 18V9M9 12.5L13 8.5l4 4" stroke="#fff" stroke-width="1.8" fill="none" stroke-linecap="round"/></svg>
      </div>
    </header>

    <section class="loan-form">
      <h2 class="project-name">New Project</h2>
      <div class="field"><span class="field-label">AMOUNT (£)</span><span class="field-value">150000,00</span></div>
      <div class="field">
        <div class="term-tabs"><span class="term-tab is-active">YEARS</span><span class="term-tab">MONTHS</span></div>
        <span class="field-value">20</span>
      </div>
      <div class="field"><span class="field-label">INTEREST % (nominal annual rate)</span><span class="field-value">3,50</span></div>
      <div class="field"><span class="field-label">INSURANCE FEES % (% of loan amount)</span><span class="field-value">0,40</span></div>
      <div class="field"><span class="field-label">ONE TIME FEES (£)</span><span class="field-value">1500,00</span></div>
    </section>

    <section class="payment-summary">
      <p class="monthly-payment">Monthly Payment : £1109,81</p>
      <div class="breakdown">
        <svg class="payment-donut" width="140" height="140" viewBox="0 0 140 140" role="img" aria-label="Payment breakdown: capital 76%, interest 20%, insurance 4%">
          <circle cx="70" cy="70" r="50" fill="var(--donut-core)"/>
          <g transform="rotate(-90 70 70)" fill="none" stroke-width="11">
            <circle cx="70" cy="70" r="56" stroke="var(--capital)" stroke-dasharray="267.4 351.9"/>
            <circle cx="70" cy="70" r="56" stroke="var(--interest)" stroke-dasharray="70.4 351.9" stroke-dashoffset="-267.4"/>
            <circle cx="70" cy="70" r="56" stroke="var(--insurance)" stroke-dasharray="14.1 351.9" stroke-dashoffset="-337.8"/>
          </g>
        </svg>
        <ul class="legend">
          <li><span class="dot insurance"></span>Insurance 4%</li>
          <li><span class="dot capital"></span>Capital 76%</li>
          <li><span class="dot interest"></span>Interest 20%</li>
        </ul>
      </div>
    </section>

    <section class="totals">
      <p>TOTAL COST OF CREDIT: £65,350,81</p>
      <p>TOTAL OF PAYMENTS: £267,453,66</p>
    </section>
    <section class="totals">
      <p>TOTAL COST OF CREDIT: £65,350,81</p>
    </section>

    <nav class="tab-bar">
      <div class="tab-item">
        <svg viewBox="0 0 24 22"><g fill="none" stroke="currentColor" stroke-width="1.4"><ellipse cx="9" cy="5" rx="5" ry="2"/><path d="M4 5v9c0 1.1 2.2 2 5 2M14 5v4"/><circle cx="16" cy="15" r="5"/></g></svg>
        <span>Capacity</span>
      </div>
      <div class="tab-item is-active">
        <svg viewBox="0 0 24 22"><g fill="none" stroke="currentColor" stroke-width="1.4"><rect x="3" y="2" width="18" height="18" rx="3"/><path d="M12 2v18M3 11h18M6 6.5h3M15 6.5h3M16.5 5v3M6 15.5h3M15 14.5h3M15 16.5h3"/></g></svg>
        <span>Loan Calculator</span>
      </div>
      <div class="tab-item">
        <svg viewBox="0 0 24 22"><g fill="none" stroke="currentColor" stroke-width="1.4"><path d="M6 2h9l4 4v14H6z"/><path d="M12.5 8l1 2 2.2.3-1.6 1.5.4 2.2-2-1-2 1 .4-2.2-1.6-1.5 2.2-.3z"/></g></svg>
        <span>Saved Loans</span>
      </div>
      <div class="tab-item">
        <svg viewBox="0 0 24 22"><g fill="none" stroke="currentColor" stroke-width="1.4"><circle cx="6" cy="11" r="2"/><circle cx="12" cy="11" r="2"/><circle cx="18" cy="11" r="2"/></g></svg>
        <span>More</span>
      </div>
    </nav>
  </main>
</body>
</html>
```